8 Page A6 booklet for Hypnosis/Hypnotherapy product

Please see PDF document attached for design brief. The booklet will be printed in http://www.pellavorn.co.uk/shop/brochures

If you do have any further questions please let me know.

This is going to be the insert for my DVD. The graphic for the DVD have now been attached to this project

Target Market(s)

People that have just purchased my Hypnosis CD

Industry/Entity Type

Hypnotherapy

Requirements
Must have
• I have attached a brief. Hopefully this explains but please do let me know if you have any further questions

```html
<!DOCTYPE html>
<html lang="en">
<head>
<meta charset="utf-8">
<title>Daniel Hartwell Hypnotherapy – 8 Page Booklet</title>
<link href="https://fonts.googleapis.com/css2?family=Montserrat:wght@500;700;800;900&family=Open+Sans:ital,wght@0,400;0,600;1,400&display=swap" rel="stylesheet">
<style>
  :root{
    --navy:#1b2a78;
    --deep:#14206a;
    --blue:#1f6fc6;
    --sky:#58aee6;
    --pale:#e3f1fb;
    --mist:#c9e3f5;
    --white:#ffffff;
    --ink:#1e2a55;
    --red:#d8262b;
    --stage:#eef0f3;
  }
  *{box-sizing:border-box;margin:0;padding:0}
  html,body{width:1200px;height:859px;overflow:hidden}
  body{background:var(--stage);font-family:"Open Sans",Arial,sans-serif;color:var(--ink)}
  .sheet{position:relative;width:1200px;height:859px}
  .spread{position:absolute;width:520px;height:366px;display:flex;box-shadow:0 10px 24px rgba(20,32,106,.22)}
  .spread--cover{left:40px;top:44px}
  .spread--about{left:640px;top:44px}
  .spread--contents{left:40px;top:470px}
  .spread--offer{left:640px;top:470px}
  .page-label{position:absolute;top:-20px;font:700 10px "Montserrat",Arial,sans-serif;color:var(--navy);letter-spacing:.5px}
  .page-label--left{left:0}
  .page-label--right{right:0}
  .page{position:relative;width:260px;height:366px;overflow:hidden;
    background:radial-gradient(ellipse at 50% 40%,var(--pale) 0%,var(--mist) 35%,var(--sky) 75%,var(--blue) 100%)}
  .page + .page{border-left:1px solid rgba(20,32,106,.18)}
  .page svg.shape{position:absolute;inset:0;width:100%;height:100%}
  .url-strip{position:absolute;left:0;right:0;bottom:0;height:24px;background:linear-gradient(90deg,var(--blue),var(--sky));
    color:var(--white);font:600 7px "Open Sans",Arial,sans-serif;letter-spacing:2px;display:flex;align-items:center;justify-content:center}
  .brand{position:absolute;display:flex;align-items:center;gap:5px}
  .brand-dot{width:14px;height:14px;border-radius:50%;background:var(--navy);flex:none}
  .brand-name{font:500 9px/1.05 "Montserrat",Arial,sans-serif;color:var(--navy);text-transform:uppercase}
  .brand--large .brand-dot{width:26px;height:26px}
  .brand--large .brand-name{font-size:14px}
  .photo{position:absolute;background:radial-gradient(circle at 50% 40%,#c9a98e 0%,#7a6a66 40%,#2b3b6b 100%)}
  .tab{position:absolute;left:50%;top:-24px;transform:translateX(-50%);width:110px;height:64px;border-radius:0 0 55px 55px;
    background:linear-gradient(var(--blue),var(--sky));display:flex;align-items:flex-end;justify-content:center;padding-bottom:12px;
    font:800 10px "Montserrat",Arial,sans-serif;color:var(--white);letter-spacing:.5px}
  .ribbon{position:absolute;left:0;right:0;height:15px;background:linear-gradient(90deg,var(--navy),var(--blue));
    color:var(--white);font:800 8px "Montserrat",Arial,sans-serif;letter-spacing:.5px;display:flex;align-items:center;justify-content:center}
  .panel{position:absolute;background:rgba(255,255,255,.55);border-radius:10px;box-shadow:0 2px 6px rgba(20,32,106,.15)}
  .body-copy{position:absolute;font-size:6px;line-height:1.4;color:var(--ink)}
  .body-copy--center{text-align:center}
  .track{display:flex;gap:8px;margin-bottom:8px}
  .track-no{font:700 6px "Montserrat",Arial,sans-serif;width:28px;flex:none;padding-top:2px}
  .track-title{font-size:7px;color:var(--blue)}
  .track-note{font-style:italic;font-size:6px}
  .disc-item{margin-bottom:4px}
  .disc-item b{color:var(--blue);font-weight:600}
  .heading{position:absolute;font:800 9px "Montserrat",Arial,sans-serif;color:var(--navy);text-transform:uppercase;letter-spacing:.4px}
  .badge{position:absolute;background:var(--navy);border-radius:3px}
  .badge--round{background:var(--blue);border-radius:50%}
</style>
</head>
<body>
<main class="sheet">

  <!-- Spread: back cover + front cover -->
  <section class="spread spread--cover">
    <span class="page-label page-label--left">PAGE 8</span>
    <span class="page-label page-label--right">PAGE 1</span>

    <article class="page page--back" style="background:var(--deep)">
      <svg class="shape" viewBox="0 0 260 366" preserveAspectRatio="none" aria-hidden="true">
        <defs>
          <linearGradient id="backBlue" x1="0" y1="0" x2="1" y2="1">
            <stop offset="0" stop-color="#2a3c9a"/><stop offset="1" stop-color="#14206a"/>
          </linearGradient>
        </defs>
        <rect width="260" height="366" fill="url(#backBlue)"/>
        <path d="M60 0 H260 V250 C210 230 190 180 150 150 C110 120 70 90 60 0 Z" fill="#f4f7fb"/>
        <path d="M60 0 C70 90 110 120 150 150 C190 180 210 230 260 250" fill="none" stroke="#58aee6" stroke-width="4"/>
      </svg>
      <div class="brand" style="left:110px;top:70px">
        <span class="brand-dot"></span>
        <span class="brand-name">Daniel Hartwell<br>Hypnotherapy</span>
      </div>
      <div class="photo" role="img" aria-label="Portrait photograph of the hypnotherapist" style="left:14px;top:188px;width:130px;height:140px;border-radius:50% 50% 10px 10px"></div>
      <div class="url-strip" style="background:linear-gradient(90deg,var(--deep),var(--blue))">DanielHartwellHypnotherapy.com</div>
    </article>

    <article class="page page--front" style="background:#f4f7fb">
      <svg class="shape" viewBox="0 0 260 366" preserveAspectRatio="none" aria-hidden="true">
        <defs>
          <linearGradient id="frontBlue" x1="0" y1="0" x2="1" y2="1">
            <stop offset="0" stop-color="#58aee6"/><stop offset="1" stop-color="#1f4fb0"/>
          </linearGradient>
        </defs>
        <path d="M200 0 C230 90 200 160 130 190 C70 215 40 270 60 366 H260 V0 Z" fill="url(#frontBlue)"/>
        <path d="M200 0 C230 90 200 160 130 190 C70 215 40 270 60 366" fill="none" stroke="#1b2a78" stroke-width="5"/>
      </svg>
      <div class="brand brand--large" style="left:36px;top:90px">
        <span class="brand-dot"></span>
        <span class="brand-name">Daniel Hartwell<br>Hypnotherapy</span>
      </div>
      <p style="position:absolute;right:18px;top:268px;text-align:right;color:var(--white);font:500 10px 'Montserrat',Arial,sans-serif">SEE PAGE 7 FOR</p>
      <p style="position:absolute;right:14px;top:282px;text-align:right;color:var(--white);font:800 11px 'Montserrat',Arial,sans-serif">EXCLUSIVE SPECIAL OFFER</p>
      <div class="url-strip" style="background:linear-gradient(90deg,var(--blue),var(--navy))">DanielHartwellHypnotherapy.com</div>
    </article>
  </section>

  <!-- Spread: page 4 + page 5 -->
  <section class="spread spread--about">
    <span class="page-label page-label--left">PAGE 4</span>
    <span class="page-label page-label--right">PAGE 5</span>

    <article class="page">
      <div class="photo" role="img" aria-label="Portrait photograph of Daniel Hartwell" style="left:50px;top:22px;width:160px;height:160px;border-radius:50%;border:4px solid var(--white);box-shadow:0 0 0 3px var(--blue)"></div>
      <div class="ribbon" style="top:196px;left:40px;right:40px;border-radius:8px 8px 0 0">DANIEL HARTWELL</div>
      <p class="body-copy body-copy--center" style="left:20px;right:20px;top:222px">Daniel is a qualified and experienced Hypnotherapist who practices in Plymouth &amp; London. He is a member of the following professional governing bodies</p>
      <div class="badge" role="img" aria-label="Professional body membership badge" style="left:56px;top:268px;width:56px;height:20px"></div>
      <div class="badge badge--round" role="img" aria-label="Professional body membership badge" style="left:158px;top:262px;width:28px;height:28px"></div>
      <div class="url-strip">DanielHartwellHypnotherapy.com</div>
    </article>

    <article class="page">
      <div class="ribbon" style="top:24px">ABOUT DANIEL</div>
      <p class="body-copy body-copy--center" style="left:16px;right:16px;top:46px">Daniel is passionate about people and sees Hypnotherapy as the most effective tool for positively impacting on our hugely powerful brains. As well as ensuring that his techniques and practices are at the cutting edge of the latest developments into the brain, he also has a huge amount of life experience including leading operations in highly stressful environments in his previous work with a national investigations unit and a regional protection service.</p>
      <div class="ribbon" style="top:136px">EXPERIENCE &amp; QUALIFICATIONS</div>
      <p class="body-copy body-copy--center" style="left:16px;right:16px;top:158px">Daniel is a fully qualified and insured Solution Focused Hypnotherapist. His products and services assist over 30,000 people every year and have reached more than 20 different countries. He is the producer of the first inflight Hypnotherapy channel in partnership with Northern Skyways. He has experience working with a wide variety of people including celebrities and high profile people. His client confidentiality is always of paramount importance.</p>
      <div class="brand" style="left:70px;top:270px">
        <span class="brand-dot"></span>
        <span class="brand-name">Daniel Hartwell<br>Hypnotherapy</span>
      </div>
      <div class="url-strip">DanielHartwellHypnotherapy.com</div>
    </article>
  </section>

  <!-- Spread: page 2 + page 3 -->
  <section class="spread spread--contents">
    <span class="page-label page-label--left">PAGE 2</span>
    <span class="page-label page-label--right">PAGE 3</span>

    <article class="page">
      <div class="tab">CONTENTS</div>
      <div class="ribbon" style="top:58px;left:50px;right:50px;border-radius:4px">CD</div>
      <div class="panel" style="left:16px;right:16px;top:80px;height:96px;padding:12px 10px">
        <div class="track">
          <span class="track-no">TRACK 1:</span>
          <div><p class="track-title">Daytime Recording -</p><p class="track-note">Use this track when you want to awaken feeling energised</p></div>
        </div>
        <div class="track">
          <span class="track-no">TRACK 2:</span>
          <div><p class="track-title">Bedtime Recording -</p><p class="track-note">Use this track when you wish to drift off to sleep after listening</p></div>
        </div>
      </div>
      <div class="ribbon" style="top:190px;left:30px;right:30px;border-radius:4px">COMPUTER DISC</div>
      <div class="panel body-copy" style="left:16px;right:16px;top:212px;height:118px;padding:14px 12px">
        <p class="disc-item"><b>Video:</b> Introduction to your recordings and some added techniques that you can use</p>
        <p class="disc-item"><b>PDF:</b> Reference document of things that you can do to accelerate your progress</p>
        <p class="disc-item"><b>MP3 versions:</b> These are the 2 CD tracks in MP3 format so that they are ready to transfer to your computer to use with your favourite listening device</p>
      </div>
      <div class="url-strip">DanielHartwellHypnotherapy.com</div>
    </article>

    <article class="page">
      <div class="ribbon" style="top:18px;left:40px">HOW TO USE</div>
      <svg style="position:absolute;left:14px;top:12px" width="24" height="24" viewBox="0 0 24 24" aria-hidden="true">
        <circle cx="12" cy="12" r="11" fill="var(--white)" stroke="var(--navy)" stroke-width="2"/>
        <rect x="7" y="8" width="10" height="8" rx="2" fill="none" stroke="var(--navy)" stroke-width="1.6"/>
        <circle cx="12" cy="12" r="1.6" fill="var(--navy)"/>
      </svg>
      <p class="body-copy body-copy--center" style="left:16px;right:16px;top:40px">The difference between the daytime and the bedtime version is the ending. There is no need to listen to both of these; the alternate endings have been provided for your convenience. Many people like to listen before bedtime and the feedback has been that they do not wish to be awoken feeling energised if they are going to go to sleep after.</p>
      <div class="ribbon" style="top:112px;left:40px">WARNING</div>
      <svg style="position:absolute;left:16px;top:128px" width="16" height="16" viewBox="0 0 16 16" aria-hidden="true">
        <circle cx="8" cy="8" r="7.5" fill="var(--red)"/>
        <rect x="7" y="3.5" width="2" height="6" fill="var(--white)"/>
        <rect x="7" y="11" width="2" height="2" fill="var(--white)"/>
      </svg>
      <p class="body-copy" style="left:38px;right:12px;top:134px">Do not listen whilst driving or operating machinery.</p>
      <div class="panel" style="left:14px;right:14px;top:154px;height:170px;background:var(--blue);border-radius:14px;border:3px solid var(--white)">
        <div role="img" aria-label="Photograph of an aircraft cabin with seatback screens" style="position:absolute;left:6px;right:6px;top:6px;height:110px;border-radius:10px;background:linear-gradient(#a7b7c8,#6d7c8f 60%,#3a4456)"></div>
        <p class="body-copy body-copy--center" style="left:10px;right:10px;top:122px;color:var(--white)">In partnership with Northern Skyways Daniel produced the first inflight hypnotherapy channel where a selection of his recordings have been made available on more than 30,000 flights worldwide</p>
      </div>
      <div class="url-strip">DanielHartwellHypnotherapy.com</div>
    </article>
  </section>

  <!-- Spread: page 6 + page 7 -->
  <section class="spread spread--offer">
    <span class="page-label page-label--left">PAGE 6</span>
    <span class="page-label page-label--right">PAGE 7</span>

    <article class="page">
      <div class="tab">FAQ'S</div>
      <svg style="position:absolute;left:100px;top:56px" width="60" height="46" viewBox="0 0 60 46" aria-hidden="true">
        <path d="M4 4 H40 V28 H18 L10 36 V28 H4 Z" fill="var(--white)" stroke="var(--navy)" stroke-width="2"/>
        <path d="M22 12 H56 V36 H50 V44 L42 36 H22 Z" fill="var(--white)" stroke="var(--navy)" stroke-width="2"/>
        <text x="39" y="31" text-anchor="middle" font-family="Montserrat, Arial, sans-serif" font-weight="800" font-size="18" fill="var(--navy)">?</text>
      </svg>
      <p class="body-copy" style="left:18px;right:18px;top:118px">Frequently asked questions (if you could keep this set out for 5 or 6 FAQ's, I will look to add the actual content for these at another time)</p>
      <p class="body-copy" style="left:18px;right:18px;top:152px">Lorem ipsum dolor sit amet, modo integre ocurreret an sea, te ubique aperiri sanctus sit. Id cum nonumy concludaturque. Pro ne oblique constituam. Sed ne veniam graeco, est ex congue aperiam laboramus. Duo everti instructior ad, harum essent corpora vis id, at meis moderatius nam.</p>
      <p class="body-copy" style="left:18px;right:18px;top:204px">Erat iusto regione sea ex, nec eu admodum reformidans. Ei zril vocibus tincidunt eum. Et corpora voluptaria sed, vel eu posse everti tamquam. Ne sea ferent inductum ocurreret. Qui cu splendide delicatissimi, inimicus constituam. Prima rebum definitionem mei no, quas tio inimicus sit an.</p>
      <div class="brand" style="left:70px;top:280px">
        <span class="brand-dot"></span>
        <span class="brand-name">Daniel Hartwell<br>Hypnotherapy</span>
      </div>
    </article>

    <article class="page">
      <p style="position:absolute;left:0;right:0;top:22px;text-align:center;font:800 18px 'Montserrat',Arial,sans-serif;color:var(--white)">EXCLUSIVE</p>
      <p style="position:absolute;left:0;right:0;top:42px;text-align:center;font:900 44px/1 'Montserrat',Arial,sans-serif;color:var(--deep)">50% <span style="font-size:20px">OFF</span></p>
      <svg style="position:absolute;left:114px;top:98px" width="32" height="32" viewBox="0 0 32 32" aria-hidden="true">
        <rect x="1" y="1" width="30" height="30" rx="6" fill="var(--blue)" stroke="var(--white)" stroke-width="2"/>
        <path d="M16 7 V19 M10 14 L16 20 L22 14" fill="none" stroke="var(--white)" stroke-width="3" stroke-linecap="round" stroke-linejoin="round"/>
        <rect x="9" y="23" width="14" height="2.5" fill="var(--white)"/>
      </svg>
      <p style="position:absolute;left:0;right:0;top:140px;text-align:center;font:600 9px 'Montserrat',Arial,sans-serif;color:var(--ink)">OF YOUR FIRST DOWNLOAD</p>
      <div style="position:absolute;left:20px;right:20px;top:168px;height:92px;border-radius:14px;border:3px solid var(--white);background:linear-gradient(var(--sky),var(--blue));box-shadow:0 3px 8px rgba(20,32,106,.3)">
        <p style="position:absolute;left:8px;right:8px;top:10px;text-align:center;font:500 8px/1.35 'Montserrat',Arial,sans-serif;color:var(--white)">Go to the website and input the following code at checkout to get 50% off</p>
        <div style="position:absolute;left:0;right:0;bottom:0;height:34px;border-radius:0 0 10px 10px;background:var(--navy);display:flex;align-items:center;justify-content:center;font:800 14px 'Montserrat',Arial,sans-serif;color:var(--white);letter-spacing:.5px">CODE: EXCLUSIVE50</div>
      </div>
      <p style="position:absolute;left:30px;right:30px;top:266px;height:16px;border-radius:0 0 8px 8px;background:var(--white);text-align:center;font:600 6.5px/16px 'Open Sans',Arial,sans-serif;color:var(--navy)">www.DanielHartwellHypnotherapy.com</p>
    </article>
  </section>

</main>
</body>
</html>
```